Packaging Design for a Bakery Shop

We are opening a Bakery Shop in the Kingdom of Bahrain where we are going to sell bread items, Cakes, sweets, etc..and we have already selected the name and the logo design (check file named Crumvela to see the logo) .

We are looking to obtain designs for our packaging mainly the following (to see the plain sample items to be used for designing see the attached files with the same names):

1. Cake Box.
2. Pastry Box.
3. Brown bakery bags.
4. White bakery bags.
5. White nylon bags.
6. Toast transparent nylon bag.
7. Coffee paper cup.
8. Napkin.
9. Stickers (this should be a sticker to be used for packaging items that can not be printable so we can use the stickers instead).

Note that priority is for the cake box and the others can have the similar theme. So for designing the above, you are kindly requested to use a base similar to the attached files not other cuts. The designer may start his submission by applying the design on the cake box.

The theme to be designed by the designer should take into consideration the fact that the colours to be used shall be matching for sweets and breads. Also as you can see in the attached logo design it is kind of mid to high product price so the theme shall match with this level.

Also the designer shall bear in mind that we want a packaging design that is easy to apply and cost effective. Maximum colours to be used for packaging should be 3 colours only.

Note that the logo colour is still not defined, so you need also to change the logo colour to make it matching with the packaging.

Regards
Tariq Hallami
+973 36412258

Target Market(s)

It is mainly women since they are the one going mainly for the bakeries. Customers are mainly walking in customers.

Industry/Entity Type

Bakery

Font styles to use
Decorative

Requirements
Must have
• The design should be unique having a new idea and not same as others.
• The design should be cost effective and can be applied in all packaging in the bakery.
• In the design we need to have some part for the instgram, tweeter, phone icons.
• It should be suitable for both bread items and sweet items.
Should not have
• No more than 3 colours design

```html
<!DOCTYPE html>
<html lang="en">
<head>
<meta charset="utf-8">
<title>Crumvela Cake Box Dieline and Sticker</title>
<link rel="stylesheet" href="https://fonts.googleapis.com/css2?family=Montserrat:wght@400;600&display=swap">
<style>
  :root{
    --bg:#f4f4f4;
    --orange:#f59a1f;
    --orange-light:#fcc13a;
    --brown:#4a1a08;
    --brown-mid:#6b2a0e;
    --cream:#ffffff;
    --cut:#8a7f78;
    --label:#4a4a4a;
  }
  html,body{margin:0;padding:0;width:1200px;height:1000px;overflow:hidden;background:var(--bg);}
  .artboard{display:block;width:1200px;height:1000px;font-family:"Montserrat",sans-serif;}
  .panel-orange{fill:url(#panelGlow);}
  .brown{fill:var(--brown);}
  .brown-mid{fill:var(--brown-mid);}
  .cream{fill:var(--cream);}
  .cutline{fill:none;stroke:var(--cut);stroke-width:1;}
  .foldline{fill:none;stroke:var(--cut);stroke-width:1;stroke-dasharray:4 3;}
  .brand-name{font-family:"Montserrat",sans-serif;font-weight:600;fill:var(--brown);}
  .brand-name-light{font-family:"Montserrat",sans-serif;font-weight:600;fill:var(--cream);}
  .brand-ring{fill:none;stroke:var(--brown);stroke-width:3;}
  .tagline{font-size:10px;fill:var(--orange);letter-spacing:1px;}
  .contact{font-size:6.5px;fill:var(--cream);}
  .contact-icon{fill:var(--cream);}
  .contact-icon-dark{fill:var(--orange);}
  .label{font-size:15px;fill:var(--label);}
  .leader{stroke:var(--label);stroke-width:.8;fill:none;}
</style>
</head>
<body>
<svg class="artboard" viewBox="0 0 1200 1000" xmlns="http://www.w3.org/2000/svg">
  <defs>
    <radialGradient id="panelGlow" cx="0.5" cy="0.5" r="0.6">
      <stop offset="0" stop-color="#fdc93b"/>
      <stop offset="1" stop-color="#f59a1f"/>
    </radialGradient>
    <linearGradient id="wheatFade" x1="0" y1="0" x2="1" y2="0">
      <stop offset="0" stop-color="#f0a23a" stop-opacity=".9"/>
      <stop offset="1" stop-color="#f59a1f" stop-opacity="0"/>
    </linearGradient>
  </defs>

  <!-- Cake box dieline -->
  <g class="dieline">
    <!-- top and bottom glue flaps (unprinted) -->
    <path class="cutline" d="M320 119 V40 H410 V35 H462 V40 H553"/>
    <path class="cutline" d="M320 561 V630 H410 V637 H462 V630 H553"/>

    <!-- lid panel -->
    <rect class="panel-orange" x="216" y="119" width="304" height="442"/>
    <path class="cutline" d="M232 119 V213 M318 119 V213 M232 460 V561 M318 460 V561 M232 213 H318 M232 460 H318"/>
    <path class="cutline" d="M410 213 V220 H462 V213 M410 460 V453 H462 V460"/>
    <rect x="470" y="500" width="50" height="61" fill="url(#wheatFade)" role="img" aria-label="Faint sketch of wheat ears and bread"/>

    <!-- small brand square on lid corner -->
    <rect x="326" y="466" width="18" height="22" fill="var(--orange-light)"/>

    <!-- upside-down contact block -->
    <g class="contact-block" transform="rotate(180 490 490)">
      <rect class="contact-icon" x="478" y="468" width="6" height="6"/>
      <text class="contact" x="487" y="473.5">+973 36412258</text>
      <rect class="contact-icon" x="478" y="478" width="6" height="6"/>
      <text class="contact" x="487" y="483.5">@crumvela</text>
      <rect class="contact-icon" x="478" y="488" width="6" height="6"/>
      <text class="contact" x="487" y="493.5">@crumvela</text>
      <rect class="contact-icon" x="478" y="498" width="6" height="6"/>
      <text class="contact" x="487" y="503.5">@crumvela</text>
    </g>

    <!-- brown spine strip -->
    <rect class="brown" x="538" y="30" width="15" height="607"/>

    <!-- patterned side panel -->
    <rect class="brown" x="553" y="119" width="107" height="442" role="img" aria-label="Dark brown panel with small golden polka dots"/>
    <rect class="brown-mid" x="645" y="119" width="15" height="442"/>

    <!-- white tagline band -->
    <rect class="cream" x="660" y="119" width="20" height="442"/>
    <text class="tagline" transform="translate(666 252) rotate(90)">Breads • Cakes • Sweets • and More.</text>

    <!-- front panel -->
    <rect class="panel-orange" x="680" y="119" width="280" height="442"/>
    <rect x="680" y="210" width="80" height="300" fill="url(#wheatFade)" role="img" aria-label="Faint sketch of wheat ears and bread loaves"/>
    <path class="cutline" d="M680 213 L660 160 M680 460 L660 520"/>
    <path class="cutline" d="M885 119 V180 Q885 213 918 213 H960 M885 561 V500 Q885 460 918 460 H960"/>
    <path class="cutline" d="M885 119 Q885 128 900 128 H945 Q960 128 960 150"/>

    <!-- brand mark on front -->
    <g class="brand" transform="translate(785 330)">
      <circle class="brand-ring" cx="0" cy="0" r="34"/>
      <text class="brand-name" x="0" y="5" font-size="15" text-anchor="middle">Crumvela</text>
    </g>
    <text class="brand-name-light" transform="translate(932 300) rotate(90)" font-size="12">Crumvela</text>

    <!-- brown end strip -->
    <rect class="brown" x="960" y="119" width="18" height="442"/>

    <!-- fold lines -->
    <path class="foldline" d="M216 213 H978 M216 460 H978"/>
  </g>

  <!-- Sticker -->
  <g class="sticker">
    <rect x="885" y="668" width="121" height="145" fill="var(--orange)"/>
    <rect x="940" y="668" width="66" height="145" fill="url(#wheatFade)" transform="scale(-1 1) translate(-1946 0)" role="img" aria-label="Faint sketch of wheat and bread"/>
    <g class="sticker-contacts">
      <rect class="contact-icon" x="894" y="719" width="8" height="8"/>
      <text class="contact" x="906" y="726" font-size="7.5">+973 36412258</text>
      <rect class="contact-icon" x="894" y="733" width="8" height="8"/>
      <text class="contact" x="906" y="740" font-size="7.5">@crumvela</text>
      <rect class="contact-icon" x="894" y="747" width="8" height="8"/>
      <text class="contact" x="906" y="754" font-size="7.5">@crumvela</text>
      <rect class="contact-icon" x="894" y="761" width="8" height="8"/>
      <text class="contact" x="906" y="768" font-size="7.5">@crumvela</text>
    </g>
    <rect class="cream" x="885" y="813" width="121" height="77"/>
    <g transform="translate(945 851)">
      <circle class="brand-ring" cx="0" cy="0" r="30"/>
      <text class="brand-name" x="0" y="5" font-size="14" text-anchor="middle">Crumvela</text>
    </g>
    <rect class="brown-mid" x="885" y="890" width="121" height="10"/>
    <path class="leader" d="M1020 784 H1112"/>
    <text class="label" x="1060" y="780">Sticker</text>
  </g>
</svg>
</body>
</html>
```